Tall Pines Restaurant & Cafe Marketing is a is a marketing company that specialises in Restaurant Marketing.
We show independent restaurant owners how to increase profits & beat their competition, we advise our customers on direct marketing methods that will help to make customers more loyal to their restaurant.
I have included some images of logos that I like the look off.
The final design should communicate that our business is professional and polished. I look forward to seeing your designs.
Restaurant

```html
<!DOCTYPE html>
<html lang="en">
<head>
<meta charset="utf-8">
<title>Tall Pines Restaurant &amp; Cafe Marketing — Business Cards</title>
<link rel="stylesheet" href="https://fonts.googleapis.com/css2?family=Source+Sans+3:wght@400;600&display=swap">
<style>
  :root {
    --page: #ffffff;
    --ink: #1c1c1c;
    --paper: #ffffff;
    --card-edge: #9a9a9a;
    --band-deep: #1c1c1c;
    --band-mid: #4a4a4a;
    --band-soft: #8c8c8c;
    --band-pale: #e6e6e6;
    --band-bright: #ffffff;
  }
  * { margin: 0; padding: 0; box-sizing: border-box; }
  html, body {
    width: 1200px;
    height: 900px;
    overflow: hidden;
    background: var(--page);
  }
  .canvas {
    position: relative;
    width: 1200px;
    height: 900px;
    font-family: "Source Sans 3", "Helvetica Neue", Arial, sans-serif;
  }
  .card {
    position: absolute;
    left: 282px;
    width: 636px;
    height: 376px;
    overflow: hidden;
  }
  .card--front {
    top: 45px;
    background: var(--paper);
    border: 1px solid var(--card-edge);
    color: var(--ink);
  }
  .card--back {
    top: 474px;
    background: var(--ink);
    color: var(--paper);
  }
  .brand {
    position: absolute;
    left: 0;
    right: 0;
    top: 104px;
    text-align center;
    text-align: center;
  }
  .brand__name {
    font-weight: 600;
    font-size: 39px;
    line-height: 1;
    letter-spacing: 0.3px;
  }
  .brand__tagline {
    margin-top: 9px;
    font-weight: 400;
    font-size: 21px;
    line-height: 1;
    letter-spacing: 4.1px;
    padding-left: 4px;
  }
  .cutlery-band {
    position: absolute;
    left: 0;
    right: 0;
    bottom: 0;
    height: 116px;
  }
  .card--front .cutlery-band {
    background: linear-gradient(180deg,
      var(--band-deep) 0%,
      var(--band-mid) 45%,
      var(--band-soft) 80%,
      var(--band-pale) 100%);
  }
  .card--back .cutlery-band {
    background: linear-gradient(180deg,
      var(--band-bright) 0%,
      var(--band-pale) 45%,
      var(--band-soft) 80%,
      var(--band-mid) 100%);
  }
</style>
</head>
<body>
  <main class="canvas">
    <section class="card card--front">
      <div class="brand">
        <p class="brand__name">Tall Pines</p>
        <p class="brand__tagline">Restaurant &amp; Cafe Marketing</p>
      </div>
      <div class="cutlery-band" role="img" aria-label="Row of black fork and knife silhouettes standing side by side along the bottom edge"></div>
    </section>

    <section class="card card--back">
      <div class="brand">
        <p class="brand__name">Tall Pines</p>
        <p class="brand__tagline">Restaurant &amp; Cafe Marketing</p>
      </div>
      <div class="cutlery-band" role="img" aria-label="Row of white fork and knife silhouettes standing side by side along the bottom edge"></div>
    </section>
  </main>
</body>
</html>
```